Internet plattform about horses with place for banners

We would like to redesign our website www.hufwelt-example.ch. We would like a simple, but modern & elegant design.
Of course the final design will be responive - but we'll start with the desktop design..

-> IMPORTANT: We will need place for 2 BANNERS: one 944x250 pixels and another 300x250px
-> We don't want any big image on the top - this takes too much place. (When we have no banners hired, we can put images of horses in place of the banners)
-> Background should be clear or white
-> Text on buttons should be text and no images
-> I would appreciate a smooth line somewhere that makes the whole design not too "rectangular"

A design we like is: www.sattelzone-example.ch (but don't do exactly the same)
-> see possible disposal of elements for top of the page -> new design.gif

On the startpage the most important are the news, as well as a new classifieds, new events .. exact content is not that important for this contest as we will offer our users possibility of choosing which content they will like.

I just upload some images you could use, but it's not a must.
If you need images, you could also take some ones on http://pferdfotos.lumbra-example.info/joomla/index.php (it's a friend of mine, so I would pay her the rights if we keep your project)

For this contest I don't expect different designs for mobile phones and don't need a css or anything else, just good ideas. Once we choose a partner this would be another job for you.

(Later, we'll work on the logo ...)

Target Market(s)

Swiss people who like horses and equestrian sports

Industry/Entity Type

Internet

Number of Pages Required

1 page

Font styles to use
Serif

Requirements
Must have
• Place for Maxiboard(944x250px) and halfpage(300x250) banners.
• The look should be modern, elegant and serious but not elitist. We should place banners for banks and other luxury sector, but all horse lovers should feel welcome. It should stay a popular site.
Nice to have
• A light element, a smooth or round line that makes the design not just rectangular...
• The design should leave much place for the information
• We leave the choice of colors open, but I like blue.. but will not be the only person to chose.
• You have the adress of our actual site (so feel free to open it - go on the contact page and send us a message,
Should not have
• no flashing design, no dark background, no big header.

```html
<!DOCTYPE html>
<html lang="en">
<head>
<meta charset="utf-8">
<title>Hufwelt – Die Schweizer Pferdeplattform</title>
<link rel="stylesheet" href="https://fonts.googleapis.com/css2?family=Open+Sans:ital,wght@0,400;0,600;0,700;1,600;1,700&family=Playball&family=Crimson+Text:ital,wght@1,600&display=swap">
<style>
:root{
  --navy:#27277a;
  --navy-bright:#3a45b0;
  --ink:#333;
  --ink-soft:#555;
  --tab:#ebebeb;
  --rule:#d6d6d6;
  --header-bg:#eeeff7;
  --band:#6a5f95;
  --footer:#3e3e3e;
  --partner-bg:#ececec;
  --accent:#f39a1d;
}
*{box-sizing:border-box;margin:0;padding:0}
html,body{width:1099px;height:1200px;overflow:hidden;background:#fff}
body{position:relative;font-family:"Open Sans",Arial,sans-serif;color:var(--ink)}
.abs{position:absolute}

/* header */
.site-header{left:0;top:0;width:1099px;height:96px;background:linear-gradient(#f3f3f8,#e6e7f2)}
.brand{left:90px;top:30px;font-size:30px;font-weight:700;color:var(--navy);line-height:1}
.tagline{left:232px;top:44px;font-size:14px;font-weight:700;font-style:italic;line-height:18px;color:#333}
.search{left:740px;top:39px;width:170px;height:28px;border:1px solid #ccc;background:#f7f7f7;font-size:11px;font-style:italic;color:#999;padding:6px 10px}
.search-btn{left:882px;top:39px;width:28px;height:28px;background:var(--navy-bright)}
.divider-v{left:923px;top:40px;width:1px;height:28px;background:#ccc}
.lang{left:938px;width:70px;height:16px;background:#dcdce4;font-size:10px;color:#444;padding-left:24px;line-height:16px}
.lang i{position:absolute;left:5px;top:4px;width:14px;height:8px}

/* hero */
.hero{left:0;top:96px;width:1099px;height:242px;background:linear-gradient(120deg,#4f4585,#7c6ea3 45%,#5a4f8c)}
.banner-main{left:53px;top:118px;width:741px;height:196px;background:#c9c6c0;padding:8px}
.banner-main .photo{width:100%;height:100%;background:linear-gradient(90deg,#8e8268,#b5ad93 50%,#6e5a48 72%,#3c3530)}
.banner-title{left:116px;top:195px;font-size:27px;font-weight:700;font-style:italic;color:#fff;line-height:34px;text-shadow:0 1px 3px rgba(0,0,0,.4)}
.arrow-btn{top:202px;width:28px;height:28px;background:rgba(50,50,50,.55)}
.banner-side{left:811px;top:118px;width:235px;height:196px;background:#c9c6c0;padding:7px}
.banner-side .photo{position:relative;width:100%;height:100%;background:linear-gradient(#3c5c9a 0 31%,#9aa0a8 31%,#d8d8d8)}
.banner-side .sponsor{position:absolute;left:0;top:0;width:100%;height:56px;display:flex;align-items:center;justify-content:center;font-size:17px;font-weight:700;color:var(--accent);line-height:1}

/* section tabs */
.tab{height:34px;background:var(--tab);border-top:5px solid var(--navy);border-radius:6px 6px 0 0;font-family:"Playball",cursive;font-size:19px;color:#222;padding-left:12px;line-height:28px}
.view-more{height:26px;border-top:1px dotted #bbb;border-bottom:1px dotted #bbb;font-size:11.5px;font-weight:700;color:#222;padding-left:11px;line-height:24px}
.view-more svg{position:absolute;right:6px;top:8px}

.thumb{width:86px;height:78px;border:1px solid #ccc;padding:3px;background:#fff}
.thumb div{width:100%;height:100%}
.news-date{font-family:"Crimson Text",serif;font-style:italic;font-weight:600;font-size:12px;color:var(--navy)}
.news-text{width:205px;font-size:11.5px;line-height:18px;color:#333}
.news-text b{font-weight:600}
.more{color:var(--navy);font-weight:700}
.sep{height:1px;border-top:1px dotted #ccc}

.offer-img{left:408px;top:419px;width:291px;height:102px;border:1px solid #ccc;padding:2px}
.offer-img div{width:100%;height:100%;background:linear-gradient(90deg,#3a7ec4,#8cc4e8 55%,#5d86b4)}
.offer-title{left:410px;top:533px;font-family:"Playball",cursive;font-size:18px;color:#222}
.offer-text{left:412px;top:561px;width:292px;font-size:11.5px;line-height:17px;color:#333}

.agenda{left:713px;top:412px;width:295px;list-style:none}
.agenda li{height:32px;border-bottom:1px solid var(--rule);font-size:12px;line-height:32px;padding-left:23px;position:relative;white-space:nowrap}
.agenda li::before{content:"";position:absolute;left:9px;top:14px;width:4px;height:4px;border-radius:50%;background:#222}
.agenda li:last-child{border-bottom:none}

/* forum */
.field{left:90px;width:434px;border:1px solid #ccc;font-size:12px;color:#555;padding:9px 10px}
.submit{left:92px;top:893px;font-size:16px;font-weight:700;color:var(--navy);letter-spacing:.5px}
.submit svg{margin-left:6px;vertical-align:middle}

/* directory */
.dir-img{left:573px;top:742px;width:187px;height:172px;border:1px solid #ccc;padding:3px}
.dir-img div{width:100%;height:100%;background:linear-gradient(160deg,#4a3a30,#a7774f 50%,#e4cfb4)}
.dir-body{left:782px;top:745px;width:262px;display:flex;flex-direction:column}
.dir-head{font-size:12px;font-weight:700;line-height:16px;color:#444;letter-spacing:.2px}
.dir-text{margin-top:9px;font-size:11.5px;line-height:20px;color:#666;letter-spacing:.2px}
.dir-more{margin-top:8px;margin-left:5px;font-size:11.5px;font-weight:700;color:#333;text-decoration:underline}

/* partners */
.partners{left:0;top:976px;width:1099px;height:100px;background:var(--partner-bg)}
.thanks{left:90px;top:1006px;font-family:"Playball",cursive;font-size:22px;line-height:26px;color:#111}
.partner{top:1000px;height:70px;background:#fff;border:1px solid #ccc;border-radius:6px;display:flex;align-items:center;justify-content:center;font-size:13px;font-weight:700;color:#3a3a3a}

/* footer */
.footer-curve{left:0;top:1060px}
.footer-brand{left:815px;top:1112px;font-size:22px;font-weight:700;color:#fff}
.social{top:1169px;width:24px;height:24px;background:#6d7bbd;border-radius:2px}
.copyright{left:93px;top:1173px;font-size:12px;color:#eee}
</style>
</head>
<body>

<header class="site-header abs"></header>
<div class="brand abs">Hufwelt</div>
<div class="tagline abs">Die schweizer pferdeplattfoem<br>La Plateforme suisse des amis du cheval</div>
<div class="search abs">Search</div>
<div class="search-btn abs">
  <svg width="28" height="28" viewBox="0 0 28 28"><circle cx="13" cy="13" r="4.5" fill="none" stroke="#fff" stroke-width="2"/><line x1="16.2" y1="16.2" x2="19.5" y2="19.5" stroke="#fff" stroke-width="2"/></svg>
</div>
<div class="divider-v abs"></div>
<div class="lang abs" style="top:36px"><i style="background:linear-gradient(90deg,#2a3fa0 33%,#fff 33% 66%,#d82a2a 66%)"></i>Francais</div>
<div class="lang abs" style="top:54px"><i style="background:linear-gradient(#111 33%,#d82a2a 33% 66%,#f5c400 66%)"></i>Deutsch</div>

<section class="hero abs" role="img" aria-label="Muted purple photograph backdrop behind the banners"></section>
<div class="banner-main abs"><div class="photo" role="img" aria-label="Banner photo: rider greeting a dark horse in an autumn field"></div></div>
<div class="banner-title abs">Discover Our Offers<br>For Professionals</div>
<div class="arrow-btn abs" style="left:76px"><svg width="28" height="28"><path d="M17 8 L10 14 L17 20Z" fill="none" stroke="#fff" stroke-width="1.3"/></svg></div>
<div class="arrow-btn abs" style="left:744px"><svg width="28" height="28"><path d="M11 8 L18 14 L11 20Z" fill="none" stroke="#fff" stroke-width="1.3"/></svg></div>
<div class="banner-side abs">
  <div class="photo" role="img" aria-label="Side banner: show jumping photography advert">
    <div class="sponsor">Pferdfotos Lumbra</div>
  </div>
</div>

<!-- news -->
<div class="tab abs" style="left:90px;top:371px;width:303px">News &amp; Articles</div>
<div class="thumb abs" style="left:91px;top:419px"><div role="img" aria-label="Horse and owner at golden sunset" style="background:linear-gradient(#e7a42a,#b0621c)"></div></div>
<div class="news-date abs" style="left:194px;top:424px">12 July, 2016</div>
<div class="news-text abs" style="left:194px;top:443px"><b>Duis autem vel eum iriure dolor</b> in hendrerit ink vulputate velitie velmil illum dolo eu feugiat`... <span class="more">[+]</span></div>
<div class="sep abs" style="left:90px;top:512px;width:300px"></div>
<div class="thumb abs" style="left:91px;top:528px"><div role="img" aria-label="Rider with dark horse under a blue sky" style="background:linear-gradient(#7ea8d8,#3d5a80)"></div></div>
<div class="news-date abs" style="left:194px;top:532px">12 July, 2016</div>
<div class="news-text abs" style="left:194px;top:551px"><b>Duis autem vel eum iriure dolor</b> in hendrerit ink vulputate velitie velmil illum dolo eu feugiat`... <span class="more">[+]</span></div>
<div class="view-more abs" style="left:90px;top:625px;width:299px">VIEW MORE<svg width="18" height="10"><path d="M0 5H15M11 1L16 5L11 9" fill="none" stroke="#222" stroke-width="2"/></svg></div>

<!-- offers -->
<div class="tab abs" style="left:407px;top:371px;width:291px">Offers</div>
<div class="offer-img abs"><div role="img" aria-label="Decorated horse beside a young rider against a bright sky"></div></div>
<div class="offer-title abs">Danse D'amour</div>
<div class="offer-text abs">Consectetuer adipiscing elit, sed diam nonummy nibh euismod tincidunt ut laoreet dolore magna aliquam erat volutpat. Ut wiugait nulla facilisi... <span class="more">[+]</span></div>
<div class="view-more abs" style="left:411px;top:625px;width:289px">VIEW MORE<svg width="18" height="10"><path d="M0 5H15M11 1L16 5L11 9" fill="none" stroke="#222" stroke-width="2"/></svg></div>

<!-- agenda -->
<div class="tab abs" style="left:713px;top:371px;width:296px">Agenda</div>
<ul class="agenda abs">
  <li>Consectetuer adipiscing elit, sed diam nonummy</li>
  <li>euismod tincidunt ut laoreet dolore magna aliqu</li>
  <li>Awisi enim ad minim veniam, quis nostrud exerci</li>
  <li>Dignissim qui blandit praesent luptatum zzril dele</li>
  <li>Ut wiugait nulla facilisi adipiscing elit</li>
  <li>Dio dignissim qui blandit praesent luptatum</li>
</ul>
<div class="view-more abs" style="left:721px;top:625px;width:289px">VIEW MORE<svg width="18" height="10"><path d="M0 5H15M11 1L16 5L11 9" fill="none" stroke="#222" stroke-width="2"/></svg></div>

<!-- forum -->
<div class="tab abs" style="left:90px;top:694px;width:434px;padding-left:19px">Forum</div>
<div class="field abs" style="top:740px;height:35px">Name</div>
<div class="field abs" style="top:778px;height:35px">Email</div>
<div class="field abs" style="top:817px;height:66px">Message</div>
<div class="submit abs">SUBMIT<svg width="18" height="10"><path d="M0 5H15M11 1L16 5L11 9" fill="none" stroke="#222" stroke-width="2"/></svg></div>

<!-- directory -->
<div class="tab abs" style="left:573px;top:694px;width:437px">Directory</div>
<div class="dir-img abs"><div role="img" aria-label="Two horses galloping in warm evening light"></div></div>
<div class="dir-body abs">
  <div class="dir-head">Lorem ipsum dolor sit amconsectetuer adipiscing elit, sed diam</div>
  <div class="dir-text">euismod tincidunt ut laoreet dolore magna aliquam erat volutpat. Ut wisi enim ad minim veniam, quis nostrud exerci tation ullamcorper suscipit lobortis nisl ut aliquip ex ea comu feugiat nulla facil.</div>
  <div class="dir-more">VIEW MORE</div>
</div>

<!-- partners -->
<div class="partners abs"></div>
<div class="thanks abs">Thank You To<br>Our Major Partners.....</div>
<div class="partner abs" style="left:328px;width:192px">Agrovet Romand</div>
<div class="partner abs" style="left:528px;width:192px">sattelzone-example.ch</div>
<div class="partner abs" style="left:729px;width:136px">Stallbau Nord</div>
<div class="partner abs" style="left:873px;width:136px">Sellerie Brun</div>

<!-- footer -->
<svg class="footer-curve abs" width="1099" height="140" viewBox="0 0 1099 140">
  <path d="M0 32 C230 110 520 115 830 18 C960 4 1050 30 1099 60 V140 H0Z" fill="var(--footer)"/>
  <path d="M0 8 C200 70 480 105 830 16 C720 30 620 75 420 85 C260 92 120 60 0 30Z" fill="var(--navy-bright)"/>
  <path d="M0 30 C120 60 260 92 420 85 C620 75 720 30 830 16 C700 40 600 84 420 92 C250 100 110 68 0 36Z" fill="#fff"/>
</svg>
<div class="footer-brand abs">Hufwelt</div>
<div class="social abs" style="left:797px" aria-label="Social network 1"></div>
<div class="social abs" style="left:829px" aria-label="Social network 2"></div>
<div class="social abs" style="left:861px" aria-label="Social network 3"></div>
<div class="social abs" style="left:893px" aria-label="Social network 4"></div>
<div class="copyright abs">Copyright © 2016 hufwelt-example.ch. All rights reserved</div>

</body>
</html>
```